Redesign of Real Estate Agency Website

We need a redesign for our real estate agency website. Please see attached creative brief.

Target Market(s)

Refer to creative brief.

Industry/Entity Type

Real Estate

Requirements
Must have
• Refer to creative brief.

```html
<!DOCTYPE html>
<html lang="en">
<head>
<meta charset="utf-8">
<title>Kaiyo Homes – Phuket Property and Real Estate</title>
<link href="https://fonts.googleapis.com/css2?family=Arimo:wght@400;700&display=swap" rel="stylesheet">
<style>
:root{
  --green-top:#8cc63f;
  --panel-green:#cfe79a;
  --blue:#1a7fcc;
  --blue-dark:#0f5fa3;
  --blue-light:#cfe6f8;
  --blue-item:#e6f2fc;
  --text:#333;
  --link:#1a6fb8;
  --red:#d42a1a;
  --orange:#e2541b;
  --grey:#e3e3e3;
  --footer:#3c3c3c;
  --footer-head:#b8e05a;
  --white:#fff;
}
*{box-sizing:border-box;margin:0;padding:0}
html,body{width:1200px;height:3258px;overflow:hidden}
body{font-family:"Arimo",Arial,sans-serif;color:var(--text);font-size:17px;line-height:1.4}
.page{position:relative;width:1200px;height:3258px;overflow:hidden;
  background:linear-gradient(180deg,var(--green-top) 0,#b5dc6a 200px,#e4efcf 600px,var(--grey) 1100px,var(--grey) 2824px,var(--footer) 2824px)}
.abs{position:absolute}
.logo-box{left:22px;top:22px;width:250px;height:163px;background:var(--white);border-radius:8px;box-shadow:0 3px 8px rgba(0,0,0,.25);text-align:center;padding-top:52px}
.logo-name{font-size:38px;font-weight:700;color:var(--blue-dark);letter-spacing:-1px;line-height:1.1}
.logo-tag{font-size:14px;color:#555;margin-top:6px}
.cart{left:985px;top:72px;font-size:14px;color:var(--blue-dark);line-height:1.35}
.cart svg{position:absolute;left:0;top:2px}
.cart div{padding-left:46px}
.cart b{color:var(--white);margin-left:22px}
.nav{left:285px;top:150px;width:915px;height:36px;background:linear-gradient(var(--blue),var(--blue-dark));display:flex;align-items:center}
.nav a{color:var(--white);font-size:15px;text-decoration:none;padding:0 16px;border-right:1px solid rgba(255,255,255,.5);line-height:36px}
.side-box{left:22px;width:255px;background:var(--blue-light);border-radius:6px;overflow:hidden;box-shadow:0 1px 3px rgba(0,0,0,.2)}
.side-head{background:linear-gradient(var(--blue),var(--blue-dark));color:var(--white);font-weight:700;font-size:17px;height:40px;line-height:40px;padding-left:14px}
.side-row{height:38px;line-height:38px;padding-left:14px;font-size:16px;border-bottom:1px solid #a9cbe6;position:relative;background:var(--blue-item)}
.side-row.arrow::after{content:"";position:absolute;right:14px;top:12px;border-left:13px solid var(--blue-dark);border-top:7px solid transparent;border-bottom:7px solid transparent}
.side-list .side-row{height:36px;line-height:36px;background:var(--white);border-bottom:1px solid #d8e6f2}
.search-row{display:flex;align-items:center;gap:10px;padding:14px}
.search-row span{display:block;width:150px;height:28px;background:var(--white);border-radius:4px}
.search-row b{font-weight:400;font-size:16px}
.map-area{margin:10px;height:240px;border-radius:4px;background:linear-gradient(#eaf3fb,#c9dff2)}
.rates{margin:10px;background:var(--white);border-radius:4px;padding:8px}
.rates-title{font-size:22px;font-weight:700;color:var(--blue-dark);border-bottom:1px solid #ccc;padding-bottom:4px}
.rates table{width:100%;border-collapse:collapse;font-size:15px}
.rates th{font-size:14px;color:#333;text-align:center;background:#e6eef6}
.rates td{text-align:center;height:24px}
.rates td:first-child{text-align:left;padding-left:8px}
.rates tr:nth-child(odd) td{background:#f1f5f9}
.rates-date{font-size:13px;display:flex;justify-content:space-between;margin-top:4px}
.rates-date a{color:var(--link)}
.share{left:64px;top:1447px;width:104px;height:22px;border:1px solid #999;border-radius:3px;background:var(--white)}
.award{left:1034px;top:204px}
.prop-panel{left:285px;top:204px;width:739px;height:1146px;background:var(--panel-green);border-radius:10px;box-shadow:0 1px 4px rgba(0,0,0,.2)}
.photo{position:absolute;border-radius:2px}
.photo-main{left:8px;top:13px;width:716px;height:452px;background:linear-gradient(180deg,#7fb0de 0%,#b7d4ea 35%,#4f8a61 55%,#6fa8c7 75%,#c9b79a 100%)}
.photo-caption{position:absolute;left:22px;top:426px;color:var(--white);font-weight:700;font-size:17px;text-shadow:0 1px 2px #000}
.thumb{top:470px;height:142px}
.more-photos{position:absolute;right:20px;top:622px;color:var(--red);font-style:normal;font-size:16px}
.mini-map{left:14px;top:660px;width:244px;height:190px;background:linear-gradient(#e9f3fb,#c3dcef);border-radius:3px}
.details{left:345px;top:662px;width:370px}
.sec-title{color:var(--blue-dark);font-weight:700;font-size:18px;margin-bottom:6px}
.kv{display:flex;font-size:16px;height:27px;line-height:27px}
.kv dt{font-weight:700;width:190px}
.details .kv{border-bottom:1px solid #b9d98a}
.fact{left:40px;top:905px;width:290px}
.fact .kv dt{font-weight:400;width:95px}
.fact .kv{height:24px;line-height:24px}
.inquiry{left:410px;top:1018px;width:200px;text-align:center}
.inquiry span{display:block;margin:0 auto 6px;width:22px;height:22px;border-radius:50%;background:var(--blue);border:4px solid var(--white);box-shadow:0 0 0 1px #999}
.inquiry b{color:var(--red);font-size:19px;border-bottom:2px solid var(--red)}
.content{left:285px;top:1358px;width:739px;height:1466px;background:var(--white);border-radius:6px;padding:22px 20px}
.content .sec-title{margin-bottom:8px}
.content p{font-size:17px;line-height:1.32;margin-bottom:10px;text-align:justify}
.inq{margin-top:20px}
.form-box{position:absolute;left:22px;top:548px;width:698px;height:361px;background:#e2effa;border-radius:6px;padding:16px 20px;font-size:14px}
.form-box p{font-size:14px;margin-bottom:8px}
.frow{display:flex;align-items:center;height:33px;font-size:14px;font-weight:700;color:var(--blue-dark)}
.frow label{width:245px}
.frow label.req{font-weight:400}
.frow span{display:block;width:282px;height:22px;background:var(--white);border:1px solid #c4d6e6}
.frow.tall{height:90px;align-items:flex-start;padding-top:6px}
.frow.tall span{height:80px}
.send{position:absolute;left:578px;top:243px;font-weight:700;color:var(--orange);font-size:17px;display:flex;align-items:center;gap:10px}
.send i{width:22px;height:22px;border-radius:50%;background:var(--blue);border:3px solid var(--white);box-shadow:0 0 0 1px #999}
.call{position:absolute;left:265px;top:320px;color:var(--red);font-size:15px}
.call em{font-style:normal;color:#333}
.browse{position:absolute;left:22px;top:930px;width:700px}
.crumbs{font-size:16px;color:#555;line-height:1.35;margin-bottom:10px}
.grid{display:grid;grid-template-columns:repeat(4,163px);column-gap:16px;row-gap:6px}
.card .img{height:102px;background:linear-gradient(#8fb8da,#6f9a6a)}
.card h4{color:var(--link);font-size:15px;margin-top:6px;white-space:nowrap;overflow:hidden}
.card div{font-size:14px;line-height:1.25}
.footer{left:0;top:2824px;width:1200px;height:434px}
.fcol{position:absolute;top:10px;font-size:14px;color:#eee;line-height:1.35}
.fcol h5{color:var(--footer-head);font-size:15px;margin-bottom:2px}
.fcol ul{list-style:none}
.fcol li::before{content:"• "}
.fcol li.sub{padding-left:30px}
.fcol li.sub::before{content:"- "}
.fsep{position:absolute;top:8px;width:1px;height:360px;background:#777}
.copy{position:absolute;right:30px;top:396px;font-size:13px;color:#ddd}
.copy b{font-weight:400;color:var(--footer-head)}
</style>
</head>
<body>
<div class="page">

  <header>
    <div class="abs logo-box">
      <div class="logo-name">Kaiyo Homes</div>
      <div class="logo-tag">Phuket Property and Real Estate</div>
    </div>
    <div class="abs cart">
      <svg width="38" height="30" viewBox="0 0 38 30"><path d="M2 3h6l5 17h18l4-12H11" fill="none" stroke="#fff" stroke-width="3"/><circle cx="15" cy="26" r="3" fill="#fff"/><circle cx="29" cy="26" r="3" fill="#fff"/></svg>
      <div>Sales inquiry cart<b>0</b></div>
      <div>Rentals inquiry cart<b>0</b></div>
    </div>
    <nav class="abs nav">
      <a>Home</a><a>Property For Sale</a><a>Property For Rent</a><a>Contact</a><a>About Us</a><a>List Your Property</a><a style="border:0">Property Buyer's Guide</a>
    </nav>
  </header>

  <aside>
    <div class="abs side-box" style="top:198px;height:312px">
      <div class="side-head">Quick Property Search</div>
      <div class="side-row arrow">Holiday Rental</div>
      <div class="side-row arrow">Property Type</div>
      <div class="side-row arrow">Region</div>
      <div class="side-row arrow">District</div>
      <div class="side-row arrow">No. of Bedrooms</div>
      <div class="search-row"><span></span><b>Search</b></div>
    </div>
    <div class="abs side-box side-list" style="top:521px;height:285px">
      <div class="side-head">Browse Property for Sale</div>
      <div class="side-row">Hot Properties &amp; Promotions</div>
      <div class="side-row">Apartments &amp; Condos</div>
      <div class="side-row">Villas &amp; Houses</div>
      <div class="side-row">Land</div>
      <div class="side-row">Commercial</div>
      <div class="side-row">Property Buyer's Guide</div>
    </div>
    <div class="abs side-box" style="top:815px;height:304px">
      <div class="side-head">Search by Map</div>
      <div class="map-area" role="img" aria-label="Clickable map of Phuket island regions for buying and renting"></div>
    </div>
    <div class="abs side-box" style="top:1130px;height:296px">
      <div class="side-head">Currency Exchange Rates</div>
      <div class="rates">
        <div class="rates-title">Exchange Rates</div>
        <table>
          <tr><th rowspan="2">Currency<br>/Baht</th><th colspan="2">Bank Notes</th></tr>
          <tr><th>Buy</th><th>Sell</th></tr>
          <tr><td>USD</td><td>29.46</td><td>30.13</td></tr>
          <tr><td>GBP</td><td>46.78</td><td>48.36</td></tr>
          <tr><td>EUR</td><td>41.13</td><td>42.33</td></tr>
          <tr><td>JPY</td><td>35.40</td><td>36.85</td></tr>
          <tr><td>HKD</td><td>3.75</td><td>3.90</td></tr>
        </table>
        <div class="rates-date"><span>07 Oct 10 at 13:50</span><a>More»</a></div>
      </div>
    </div>
    <div class="abs share"></div>
  </aside>

  <svg class="abs award" width="161" height="651" viewBox="0 0 161 651" role="img" aria-label="Property award ribbon">
    <path d="M0 0h161v651l-80.5-60L0 651z" fill="#1e1e1e"/>
  </svg>

  <main>
    <section class="abs prop-panel">
      <div class="photo photo-main" role="img" aria-label="Villa terrace with sun loungers, umbrellas and sea view"></div>
      <div class="photo-caption">Magnificent Sea View Villa</div>
      <div class="photo thumb" style="left:8px;width:228px;background:linear-gradient(#8fb6d8,#5b8f73)" role="img" aria-label="Pool and bay view"></div>
      <div class="photo thumb" style="left:244px;width:232px;background:linear-gradient(#d8c7a8,#8a6d4b)" role="img" aria-label="Villa living room"></div>
      <div class="photo thumb" style="left:484px;width:240px;background:linear-gradient(#2d4b7a,#c9733c)" role="img" aria-label="Villa pool at dusk"></div>
      <em class="more-photos">More Photos</em>
      <div class="photo mini-map" role="img" aria-label="Location map of Kamala on Phuket island"></div>
      <div class="abs details">
        <div class="sec-title">Property Details</div>
        <dl>
          <div class="kv"><dt>Land Area</dt><dd>2313</dd></div>
          <div class="kv"><dt>Built-up Area</dt><dd>786</dd></div>
          <div class="kv"><dt>Bedrooms</dt><dd>6</dd></div>
          <div class="kv"><dt>Bathrooms</dt><dd>6</dd></div>
          <div class="kv"><dt>Swimming Pool</dt><dd>Private</dd></div>
          <div class="kv"><dt>Jacuzzi</dt><dd>Outdoor</dd></div>
          <div class="kv"><dt>Car Parking</dt><dd>Shared</dd></div>
          <div class="kv"><dt>Furnished</dt><dd>Fully-furnished</dd></div>
          <div class="kv"><dt>Ownership Structure</dt><dd>Leasehold</dd></div>
        </dl>
      </div>
      <div class="abs fact">
        <div class="sec-title">Fact Sheet</div>
        <dl>
          <div class="kv"><dt>Price</dt><dd>USD 5.95M</dd></div>
          <div class="kv"><dt>Type</dt><dd>Villa</dd></div>
          <div class="kv"><dt>Location</dt><dd>Kamala, West</dd></div>
          <div class="kv"><dt></dt><dd>Phuket</dd></div>
          <div class="kv"><dt>View</dt><dd>Sea View</dd></div>
          <div class="kv"><dt>Ref. no.</dt><dd>1583</dd></div>
        </dl>
      </div>
      <div class="abs inquiry"><span></span><b>MAKE INQUIRY</b></div>
    </section>

    <section class="abs content">
      <div class="sec-title">Description</div>
      <p>A one of a kind exclusive villa, constructed over three levels. Built to the award-winning standards of a highly reputable international developer, and offers the very highest of standards of build materials and design to maximise living spaces using natural light, while retaining a number of contemporary and original Thai features.</p>
      <p>Private entrance gate with granite stone walls, and planters leading to upper level with undercover walkway, private 18 metre lap swimming pool with inset Jacuzzi, covered dining sala, master bedroom suite with dressing room and en-suite bathroom, family room, dining room, cloakroom, kitchen/breakfast room, separate Asian wet kitchen, laundry room, maids quarter, undercover walkway to elevator. A MUST SEE!</p>
      <div class="sec-title inq">Inquire About this Property</div>
      <p>To request more information about this property, please provide us with your email address, name and any questions that you might have. We will respond within 24 hours.</p>
      <p>We look forward to assisting you.</p>
      <p>To submit an inquiry for multiple properties click "Add to Inquiry Cart". You will be taken the Inquiry Cart page where you can review items and then continue to inquiry form or add more properties.</p>

      <div class="form-box">
        <p>Alternatively, to submit an inquiry for this property only, complete the form below and click "Send".</p>
        <div class="frow"><label class="req">* indicates a required field.</label><span></span></div>
        <div class="frow"><label>Your name *</label><span></span></div>
        <div class="frow"><label>Your email *</label><span></span></div>
        <div class="frow"><label>Country of residence</label><span></span></div>
        <div class="frow"><label>Phone number</label><span></span></div>
        <div class="frow tall"><label>Comments</label><span></span></div>
        <div class="send"><i></i>Send</div>
        <div class="call">Or call us on <em>+66 (0) 812 345 678</em></div>
      </div>

      <div class="browse">
        <div class="sec-title">Browse more properties:</div>
        <div class="crumbs">Villas &amp; Houses<br>West Phuket<br>West Phuket / Kamala Property</div>
        <div class="grid">
          <div class="card"><div class="img" role="img" aria-label="Villa interior"></div><h4>Amara Villa</h4><div>Patong<br>Villa<br>THB 17.5M</div></div>
          <div class="card"><div class="img" role="img" aria-label="Thai style house"></div><h4>Baan Rim Surin ...</h4><div>Surin<br>Villa<br>THB 25.5M</div></div>
          <div class="card"><div class="img" role="img" aria-label="Villa with pool"></div><h4>The Crest Kamala</h4><div>Kamala<br>Villa<br>THB 14.6M - 17.4M</div></div>
          <div class="card"><div class="img" role="img" aria-label="Villa with garden"></div><h4>Baan Talay Sai</h4><div>Patong<br>Villa<br>THB 45M - 50M</div></div>
          <div class="card"><div class="img" role="img" aria-label="Sea view villa"></div><h4>Magnificent ...</h4><div>Patong<br>Villa<br>THB 45M - 50M</div></div>
          <div class="card"><div class="img" role="img" aria-label="Hillside villa"></div><h4>Ruen Sabai</h4><div>Kalim<br>Villa<br>THB 35M</div></div>
          <div class="card"><div class="img" role="img" aria-label="Evening view villa"></div><h4>Dusk View Villa ...</h4><div>Surin<br>Villa<br>THB 120M</div></div>
          <div class="card"><div class="img" role="img" aria-label="Villa complex"></div><h4>Orchid Bay Villas</h4><div>Patong<br>Villa<br>USD 1.5M - 2M</div></div>
        </div>
      </div>
    </section>
  </main>

  <footer class="abs footer">
    <div class="fcol" style="left:41px">
      <h5>phuket real estate for sale</h5>
      <ul>
        <li>phuket property for sale index</li>
        <li>search property for sale in phuket</li>
        <li>apartments &amp; condos for sale in phuket</li>
        <li>villas &amp; houses for sale in phuket</li>
        <li>land for sale in phuket</li>
        <li>commercial property for sale in phuket</li>
        <li>luxury property for sale</li>
        <li>property for sale map</li>
        <li>property buyer's guide for phuket</li>
        <li class="sub">why phuket?</li>
        <li class="sub">property ownership rights</li>
        <li class="sub">property taxes &amp; fees</li>
        <li class="sub">land titles</li>
        <li class="sub">land units</li>
        <li class="sub">property faq</li>
      </ul>
    </div>
    <div class="fsep" style="left:372px"></div>
    <div class="fcol" style="left:388px">
      <h5>phuket property for rent</h5>
      <ul>
        <li>phuket property for rent index</li>
        <li>search property for rent in phuket</li>
        <li>phuket holiday rentals</li>
        <li class="sub">holiday villas</li>
        <li class="sub">luxury villas</li>
        <li class="sub">cheap villas</li>
        <li class="sub">holiday apartments</li>
        <li class="sub">holiday rentals booking guide</li>
        <li class="sub">holiday rentals faq</li>
        <li class="sub">terms &amp; conditions</li>
        <li>samui holiday rentals</li>
        <li>phuket long-term rentals</li>
        <li class="sub">long-term villas &amp; houses</li>
        <li class="sub">long-term apartments</li>
        <li>property for rent map</li>
      </ul>
    </div>
    <div class="fsep" style="left:690px"></div>
    <div class="fcol" style="left:706px">
      <h5>site links</h5>
      <ul>
        <li>kaiyo homes real estate index</li>
        <li>privacy policy</li>
        <li>disclaimer</li>
        <li>site map</li>
      </ul>
      <h5 style="margin-top:8px">about kaiyo homes real estate</h5>
      <ul>
        <li>about us</li>
        <li>contact us</li>
        <li>list your property</li>
        <li class="sub">selling your property</li>
      </ul>
    </div>
    <div class="fsep" style="left:956px"></div>
    <div class="fcol" style="left:972px">
      <h5>phuket info</h5>
      <ul>
        <li>kaiyo homes homepage</li>
        <li>travel info</li>
        <li>tours</li>
        <li>dining &amp; nightlife</li>
        <li>expats</li>
        <li>directory</li>
        <li>classified ads</li>
        <li>hotels</li>
      </ul>
    </div>
    <div class="copy">Phuket Real Estate from Kaiyo Homes &nbsp;|&nbsp; <b>Copyright © Kaiyo Homes 2009.</b> All Rights Reserved</div>
  </footer>

</div>
</body>
</html>
```